Realty Group Needs Classy, Contemporary Letterhead Design

We need a letterhead design for a new realty company located in NY, USA. We buy investment properties to rehabilitate and or keep in our rental portfolio.

```html
<!DOCTYPE html>
<html lang="en">
<head>
<meta charset="utf-8">
<title>Meridian Holdings – Letterhead</title>
<link href="https://fonts.googleapis.com/css2?family=Saira:ital,wght@0,300;0,400;0,800;1,300&display=swap" rel="stylesheet">
<style>
  :root {
    --purple: #4b2a86;
    --purple-soft: #5b3c97;
    --ink: #3b3b40;
    --backdrop: #e0d3fd;
    --paper: #ffffff;
    --emblem-tint: #e8e5f2;
    --signature-tint: #ece6f7;
    --on-band: #ffffff;
  }
  * { margin: 0; padding: 0; box-sizing: border-box; }
  html, body {
    width: 1200px; height: 991px; overflow: hidden;
    background: var(--backdrop);
    font-family: "Saira", sans-serif;
  }
  .letterhead {
    position: absolute; left: 267px; top: 25px;
    width: 665px; height: 940px;
    background: var(--paper);
    overflow: hidden;
  }
  .emblem-wash {
    position: absolute; left: 0; top: 520px;
    width: 360px; height: 420px;
    background: radial-gradient(ellipse at 25% 75%, var(--emblem-tint) 0%, var(--emblem-tint) 35%, rgba(232,229,242,0) 72%);
  }
  .brand {
    position: absolute; top: 62px; left: 0; width: 100%;
    text-align: center;
    font-weight: 800; font-size: 40px; line-height: 1; letter-spacing: -0.5px;
    color: var(--purple);
  }
  .sender { position: absolute; left: 74px; top: 204px; }
  .sender-name {
    font-weight: 800; font-size: 28px; line-height: 1;
    color: var(--purple); letter-spacing: 0;
  }
  .sender-role {
    margin-top: 6px;
    font-weight: 300; font-size: 20px; line-height: 1;
    color: var(--purple-soft);
  }
  .letter-date {
    position: absolute; right: 73px; top: 249px;
    font-weight: 300; font-size: 15px;
    color: var(--purple-soft);
  }
  .letter-body {
    position: absolute; left: 66px; top: 298px; width: 531px;
    font-weight: 300; font-size: 13.4px; line-height: 28.5px; letter-spacing: 0.25px;
    color: var(--ink);
    text-align: justify;
  }
  .signature {
    position: absolute; left: 433px; top: 720px;
    width: 152px; height: 48px;
    border-radius: 24px;
    background: linear-gradient(90deg, rgba(236,230,247,0.2), var(--signature-tint), rgba(236,230,247,0.2));
  }
  .signature-name {
    position: absolute; left: 430px; top: 788px; width: 160px;
    text-align: center;
    font-style: italic; font-weight: 300; font-size: 17px;
    color: var(--purple-soft);
  }
  .contact-band {
    position: absolute; left: 191px; right: 0; top: 888px; height: 30px;
    background: var(--purple);
    display: flex; align-items: center; justify-content: space-around;
    padding: 0 6px;
    color: var(--on-band); font-weight: 300; font-size: 12px;
  }
  .contact-item { display: flex; align-items: center; gap: 5px; white-space: nowrap; }
  .contact-item svg { width: 11px; height: 11px; fill: none; stroke: var(--on-band); stroke-width: 1.6; }
</style>
</head>
<body>
  <main class="letterhead">
    <div class="emblem-wash" role="img" aria-label="Faint brand decoration area"></div>

    <header class="brand">Meridian Holdings</header>

    <section class="sender">
      <h1 class="sender-name">NAME SURNAME</h1>
      <p class="sender-role">MANAGER</p>
    </section>
    <p class="letter-date">Dec. 28, 2021</p>

    <article class="letter-body">
      <p>Lorem ipsum dolor sit amet, consectetuer adipiscing elit, sed diam nonummy nibh euismod tincidunt ut laoreet dolore magna aliquam erat volutpat. Ut wisi enim ad minim veniam, quis nostrud exerci tation ullamcorper suscipit lobortis nisl ut aliquip ex ea commodo consequat. qui blandit praesent luptatum zzril delenit augue duis dolore te feugait nulla facilisi.</p>
      <p>Lorem ipsum dolor sit amet, cons ectetuer adipiscing elit, sed diam nonummy nibh euismod tincidunt ut laoreet dolore magna aliquam erat volutpat. Ut wisi enim ad minim veniam, quis nostrud exerci tation ullamcorper suscipit lobortis nisl ut aliquip ex ea commodo consequat.</p>
      <p>Lorem ipsum dolor sit amet, consectetuer adipiscing elit, sed diam nonummy nibh euismod tincidunt ut laoreet dolore magna aliquam erat volutpat. Ut wisi enim ad minim veniam,vel illum dolore eu feugiat nulla facilisis at vero eros et accumsan et iusto odio dignissim qui blandit praesent luptatum zzril delenit augue duis dolore te feugait nulla facilisi.</p>
    </article>

    <div class="signature" role="img" aria-label="Handwritten signature"></div>
    <p class="signature-name">LOREM IPSUM</p>

    <footer class="contact-band">
      <span class="contact-item">
        <svg viewBox="0 0 12 12"><rect x="1" y="2.5" width="10" height="7" rx="1"/><path d="M1.5 3 L6 6.5 L10.5 3"/></svg>
        hello@meridianholdings.com
      </span>
      <span class="contact-item">
        <svg viewBox="0 0 12 12"><path d="M3 1.5 L4.8 4 L3.8 5.2 C4.5 6.8 5.2 7.5 6.8 8.2 L8 7.2 L10.5 9 L9.5 10.5 C5.5 10.5 1.5 6.5 1.5 2.5 Z"/></svg>
        +1 212 555 0147
      </span>
      <span class="contact-item">
        <svg viewBox="0 0 12 12"><circle cx="6" cy="6" r="4.8"/><ellipse cx="6" cy="6" rx="2" ry="4.8"/><path d="M1.2 6 H10.8"/></svg>
        www.meridianholdings.com
      </span>
    </footer>
  </main>
</body>
</html>
```